Muay Thai gym needs an KICK-A$$ NEW timetablefor classes

Kroa Ren is Canberra's home of authentic Muay Thai, and we need a new timetable for our ever expanding list of classes!<br/><br/>A document containing all classes & information is included, as well as our logo in .png and .eps formats.

Font styles to use
Serif
Sans Serif

Colors

Designer to choose colors to be used in the design.

```html
<!DOCTYPE html>
<html lang="en">
<head>
<meta charset="utf-8">
<title>Kroa Ren – Class Timetable</title>
<link rel="stylesheet" href="https://fonts.googleapis.com/css2?family=Carlito:wght@400;700&display=swap">
<style>
:root{
  --green:#056b38;
  --white:#ffffff;
}
*{margin:0;padding:0;box-sizing:border-box}
html,body{width:1200px;height:849px;overflow:hidden;background:var(--white)}
.timetable{position:relative;width:1200px;height:849px;font-family:"Carlito",sans-serif;color:var(--white)}
.masthead{position:absolute;left:0;top:0;width:1200px;height:309px;background:var(--white)}
.brand-name{position:absolute;left:0;top:70px;width:1200px;text-align:center;font-weight:700;font-size:118px;line-height:1;color:var(--green);letter-spacing:6px}
.address{position:absolute;left:0;top:274px;width:1200px;text-align:center;font-weight:700;font-size:25px;line-height:1;color:var(--green);letter-spacing:1.6px;padding-left:10px}
.schedule{position:absolute;left:0;top:309px;width:1200px;height:540px;background:var(--green)}
.day{position:absolute}
.day h2{font-weight:700;font-size:22.5px;line-height:1;margin-bottom:18px}
.day ul{list-style:none}
.day li{font-size:14.2px;line-height:17.5px;white-space:nowrap}
.day li .indent{display:block;padding-left:132px}
.day p{font-size:14.2px;line-height:17.5px;width:340px}
.mon{left:41px;top:35px}
.tue{left:41px;top:232px}
.wed{left:448px;top:35px}
.thu{left:447px;top:232px}
.fri{left:838px;top:35px}
.sat{left:838px;top:150px}
.sun{left:838px;top:319px}
.contact{position:absolute;top:436px;display:flex;align-items:center;gap:12px}
.contact svg{width:52px;height:52px;flex:none}
.contact span{font-weight:700;font-size:16px;letter-spacing:2.2px}
.web{left:29px}
.social-a{left:436px}
.social-b{left:827px}
</style>
</head>
<body>
<main class="timetable">
  <header class="masthead">
    <div class="brand-name">KROA REN</div>
    <div class="address">LEVEL 1, 48 HARWOOD STREET, BELTANA, CANBERRA</div>
  </header>

  <section class="schedule">
    <div class="day mon">
      <h2>Monday</h2>
      <ul>
        <li>6:00 AM – 6:45 AM – Muay Thai (All Experience)</li>
        <li>4:30 PM – 5:15 PM – Junior &amp; Teenage Muay Thai</li>
        <li>5:30 PM – 6:30 PM – Muay Thai (All Experience)</li>
        <li>5:30 PM – 6:30 PM – Muay Thai for Beginners</li>
        <li>6:30 PM – 7:30 PM – Padwork</li>
        <li>7:30 PM – 8:00 PM – Sparring (Must do Padwork)</li>
      </ul>
    </div>

    <div class="day tue">
      <h2>Tuesday</h2>
      <ul>
        <li>6:00 AM – 6:45 AM – Fighters</li>
        <li>1:00 PM – 1:45 PM – Muay Thai (All Experience)</li>
        <li>4:30 PM – 5:15 PM – Junior &amp; Teenage Muay Thai</li>
        <li>5:30 PM – 6:30 PM – Padwork</li>
        <li>6:00 PM – 7:30 PM – Muay Thai<span class="indent">(Development, Intermediate and Fighters)</span></li>
        <li>6:30 PM – 7:30 PM - Muay Thai</li>
      </ul>
    </div>

    <div class="day wed">
      <h2>Wednesday</h2>
      <ul>
        <li>6:00 AM – 6:45AM – Muay Thai (All Experience)</li>
        <li>5:30 PM – 6:30PM – Muay Thai (All Levels)</li>
        <li>5:30 PM – 6:30PM – Muay Thai for Beginners</li>
        <li>6:30 PM – 7:30PM – Padwork</li>
        <li>7:30 PM – 8:00PM – Sparring (Must do Padwork)</li>
      </ul>
    </div>

    <div class="day thu">
      <h2>Thursday</h2>
      <ul>
        <li>6:00 AM – 7:00 AM – Fighters</li>
        <li>1:00 PM – 1:45 PM – Muay Thai (All Experience)</li>
        <li>4:30 PM – 5:15 PM – Junior &amp; Teenage Muay Thai</li>
        <li>5:30 PM – 6:30 PM – Padwork</li>
        <li>6:00 PM – 7:30 PM – Muay Thai<span class="indent">(Development, Intermediate &amp; Fighters)</span></li>
        <li>6:30 PM – 7:30 PM - Beginners Sparring &amp; Clinching</li>
      </ul>
    </div>

    <div class="day fri">
      <h2>Friday</h2>
      <ul>
        <li>6:00 AM – 6:45 AM – Muay Thai (All Experience)</li>
      </ul>
    </div>

    <div class="day sat">
      <h2>Saturday</h2>
      <ul>
        <li>8:00 AM – 8:45 AM – Muay Thai</li>
        <li>9:00 AM - 10:30 AM – Fighters</li>
        <li>11:00 AM – 11:45 AM – Junior &amp; Teenage Muay Thai</li>
        <li>12:00 PM – 1:00 PM – Muay Thai (All Experience)</li>
      </ul>
    </div>

    <div class="day sun">
      <h2>Sunday</h2>
      <p>Personal training available seven days a week, including Sunday!</p>
    </div>

    <div class="contact web">
      <svg viewBox="0 0 52 52" aria-hidden="true">
        <circle cx="26" cy="26" r="25" fill="var(--white)"/>
        <g fill="none" stroke="var(--green)" stroke-width="3">
          <circle cx="26" cy="26" r="18"/>
          <ellipse cx="26" cy="26" rx="8" ry="18"/>
          <line x1="8" y1="26" x2="44" y2="26"/>
          <line x1="11" y1="17" x2="41" y2="17"/>
          <line x1="11" y1="35" x2="41" y2="35"/>
        </g>
      </svg>
      <span>www.kroaren.com.au</span>
    </div>
    <div class="contact social-a">
      <svg viewBox="0 0 52 52" aria-hidden="true"><circle cx="26" cy="26" r="25" fill="var(--white)"/></svg>
      <span>linkhub.net/kroarencanberra</span>
    </div>
    <div class="contact social-b">
      <svg viewBox="0 0 52 52" aria-hidden="true"><circle cx="26" cy="26" r="25" fill="var(--white)"/></svg>
      <span>snapgrid.net/kroarencanberra</span>
    </div>
  </section>
</main>
</body>
</html>
```